Maple Crest Table Business Cards

We need Business cards development for our expanding business. Our Company MapleCrestTable promotes grain free living through products, services and healthy living concepts. Our Products are:
Non-Grain
Non- GMO
Non- Soy
Gluten-Free

Reason: We will need to extend the deadline on our Business Card contest. Thanks, MCT

Industry/Entity Type

Business

```html
<!DOCTYPE html>
<html lang="en">
<head>
<meta charset="utf-8">
<title>Maple Crest Table Business Card</title>
<link rel="stylesheet" href="https://fonts.googleapis.com/css2?family=Arimo:wght@400;700&family=Michroma&display=swap">
<style>
  :root {
    --backdrop: #4a4a4a;
    --card-white: #ffffff;
    --leaf-green: #8cc63f;
    --deep-green: #1f6b35;
    --brand-green: #2e8b3c;
    --ink: #1a1a1a;
    --icon-bg: #2d5a2a;
  }
  * { margin: 0; padding: 0; box-sizing: border-box; }
  html, body {
    width: 1200px; height: 1000px; overflow: hidden;
    background: var(--backdrop);
    font-family: "Arimo", Arial, sans-serif;
  }
  .business-card {
    position: absolute; left: 246px; top: 293px;
    width: 707px; height: 413px;
    background: var(--card-white);
    box-shadow: 0 2px 6px rgba(0,0,0,0.35);
    overflow: hidden;
  }
  .card-band {
    position: absolute; left: 0; top: 0; width: 100%; height: 263px;
    background: var(--leaf-green);
  }
  .holder {
    position: absolute; left: 60px; top: 130px; width: 280px;
    text-align: center;
  }
  .holder-name {
    font-family: "Michroma", "Arimo", sans-serif;
    font-size: 25px; font-weight: 700; color: var(--deep-green);
    letter-spacing: 0.5px;
  }
  .holder-role {
    margin-top: 4px; font-size: 18px; color: #2f5a24;
  }
  .contact-list {
    position: absolute; left: 398px; top: 100px; list-style: none;
  }
  .contact-item {
    display: flex; align-items: center; height: 28.5px;
    font-size: 18px; color: var(--ink);
  }
  .contact-icon {
    width: 16px; height: 16px; margin-right: 10px; flex: none;
  }
  .brand {
    position: absolute; left: 0; top: 263px; width: 100%; height: 150px;
    display: flex; align-items: center; justify-content: center;
  }
  .brand-dot {
    width: 54px; height: 54px; border-radius: 50%;
    background: var(--brand-green); margin-right: 22px;
  }
  .brand-name {
    font-size: 47px; font-weight: 700; color: var(--brand-green);
    letter-spacing: -0.5px; line-height: 1;
  }
</style>
</head>
<body>
  <article class="business-card">
    <div class="card-band"></div>

    <div class="holder">
      <div class="holder-name">Adrian Mercer</div>
      <div class="holder-role">CEO / Founder</div>
    </div>

    <ul class="contact-list">
      <li class="contact-item">
        <svg class="contact-icon" viewBox="0 0 16 16"><rect width="16" height="16" rx="3" fill="var(--icon-bg)"/><rect x="5" y="3" width="6" height="10" rx="1" fill="none" stroke="#fff" stroke-width="1.4"/><circle cx="8" cy="11" r="0.8" fill="#fff"/></svg>
        +1 555.210.4471
      </li>
      <li class="contact-item">
        <svg class="contact-icon" viewBox="0 0 16 16"><rect width="16" height="16" rx="3" fill="var(--icon-bg)"/><path d="M5 3.5c-1 1-1 3 1 5.5s4.5 3.5 5.5 2.5l0.5-1.2-2-1.3-1 0.8c-1-0.5-2-1.5-2.6-2.6l0.8-1-1.3-2z" fill="#fff"/></svg>
        +1 555.210.4471
      </li>
      <li class="contact-item">
        <svg class="contact-icon" viewBox="0 0 16 16"><rect width="16" height="16" rx="3" fill="var(--icon-bg)"/><rect x="3.5" y="5" width="9" height="6.5" fill="none" stroke="#fff" stroke-width="1.2"/><path d="M3.5 5l4.5 3.5 4.5-3.5" fill="none" stroke="#fff" stroke-width="1.2"/></svg>
        contact@samplemail.com
      </li>
      <li class="contact-item">
        <svg class="contact-icon" viewBox="0 0 16 16"><rect width="16" height="16" rx="3" fill="var(--icon-bg)"/><circle cx="8" cy="8" r="4.8" fill="none" stroke="#fff" stroke-width="1.1"/><ellipse cx="8" cy="8" rx="2" ry="4.8" fill="none" stroke="#fff" stroke-width="1"/><path d="M3.2 8h9.6" stroke="#fff" stroke-width="1"/></svg>
        www.samplesite.com
      </li>
    </ul>

    <div class="brand">
      <div class="brand-dot"></div>
      <div class="brand-name">MapleCrestTable</div>
    </div>
  </article>
</body>
</html>
```